Verantis Guest Event Collateral

Create a double-sided, oversized piece of collateral for a series of guest networking events that we'll be hosting in 2019

We are looking for this piece of collateral to be the size of an oversized post card (1/2 of an 8/5 x 11 piece of paper). The front should include the following: Verantis's Mission Statement: Continually foster a culture of community and education for focused business professionals. How do we do it? Using four distinct principles, Verantis offers business professionals the opportunity to be successful right now ,as well as next year. Through in-person meetings, virtual meetings, networking events, and educational opportunities Verantis offers members a chance to hit their goals not only this year, but every year! Collaboration: Work with like-minded, driven Verantis members to collaborate and overcome the objections, hurdles and challenges that all business professionals face, either in person at twice monthly meetings, or virtually, from the comfort of your home or office. Accountability: Stay on track, and complete the goals you have set for yourself! Weekly in person or virtual meetings afford all members the opportunity to review their plan twice a month with fellow Verantis members, and trained Verantis coaches. Referrals: In the midst of crafting an executable, measurable and attainable plan let Verantis build your business through a steady stream of referrals via six yearly networking events, specifically designed to ensure you walk away with new referral partners. Strategy: Let Verantis assist you in crafting a strategy within our proven business planning template; realistic, understandable, measurable, beyond normal, attainable and time bound. The back should include the following: Become a Verantis member for $150/month and join us for 6 Networking Events in 2019 plus much more! We aren’t just about collaboration, accountability and strategy! Creating opportunities for referrals is also a cornerstone of Verantis! To make certain we are delivering on this principle, Verantis will host 6 events throughout 2019, complete with specific activities at each event to ensure you meet everyone in the room, making immediate connects to build your referral network. Join now and put yourself in position for success in 2019! Name: Phone: Email: Company Name: Industry: Position: Credit Card Number: Exp. Date: Testimonials: Overall I think people are lazy. I know I am! The benefits I have found and have come to truly appreciate thru Verantis are a sense of professionalism, accountability and shared enthusiasm. These things break that cycle of laziness for me and, I am sure, many others. When I walk into a meeting I know that positive and helpful feedback is the name of the game. Feedback from others and in many other industries from my own has become a key and cornerstone to my business and personal success. I would urge anyone no matter what your occupation to attend a couple of meetings and see how this group of like minded professionals can help you to achieve more. More time, More success, More health, More security, More money, More happiness..............What could you use more of? Gordon T. Melby Sr. Automotive Consultant Ridgewater Leasing & Sales Thank you!

Target Market(s)

Small business owners, entrpreneurs, networkers, sales people

Industry/Entity Type

Business Consultant

Font styles to use
Sans Serif

Colors
f36f22
f68d4e
f8ba93
f78f20
faa54b

Requirements
Must have
• - Imagery
• - Our company logo
• - Clear CTA to check out our website (www.verantis-example.com)
• - Option to "Join the Verantis Community Today!" and include a spot for someone to fill in their name, email address, company name, and phone number
• - Reference that we host 6+ networking events in Denver throughout the year that are free to attend and are unlike any other networking event they've attended before
• - Mention that we have in-person meetings 2x per month, virtual meeting options, networking events, and educational events
• - Highlight the following acronym which references our core company components:
• Collaboration:
• Work with like-minded, driven Verantis members to collaborate and overcome the objections, hurdles and challenges that all business professionals face, in either in person twice monthly meetings, or virtually, from the comfort of your home of office.
• Accountability:
• Stay on track, and complete the goals you have set for yourself! Weekly in person or virtual meetings afford all members the opportunity to review their plan twice a month with your fellow Verantis members and trained Verantis coaches, to make certain you success is continuous throughout the year.
• Referrals:
• In the midst of crafting an executable, measurable and attainable plan let Verantis build your business through a steady stream of referral opportunities via twelve yearly networking events, specifically designed to ensure you walk away with new referral partners.
• Strategy:
• Let Verantis assist you in crafting a strategy within our proven business planning template; realistic, understandable, measurable, beyond normal, attainable and time bound.

```html
<!DOCTYPE html>
<html lang="en">
<head>
<meta charset="utf-8">
<title>Verantis Guest Event Collateral</title>
<link rel="stylesheet" href="https://fonts.googleapis.com/css2?family=Montserrat:wght@300;400;500;600;700&display=swap">
<style>
  :root {
    --orange: #f78f20;
    --orange-deep: #f36f22;
    --orange-soft: #faa54b;
    --orange-pale: #f8ba93;
    --charcoal: #4a4a4a;
    --charcoal-dark: #2e2e2e;
    --ink: #222222;
    --paper: #ffffff;
    --backdrop: #cfcfcf;
  }
  * { margin: 0; padding: 0; box-sizing: border-box; }
  html, body { width: 960px; height: 1200px; overflow: hidden; }
  body {
    background: radial-gradient(circle at 50% 45%, #e4e4e4, var(--backdrop));
    font-family: "Montserrat", sans-serif;
    position: relative;
  }
  .sheet {
    position: absolute;
    top: 295px;
    width: 473px;
    height: 670px;
    transform: scale(0.909);
    transform-origin: top left;
    overflow: hidden;
    box-shadow: 0 10px 28px rgba(0,0,0,.35);
  }
  .sheet--front { left: 40px; background: var(--charcoal); }
  .sheet--back { left: 490px; background: var(--paper); }
  .sheet svg.shapes { position: absolute; inset: 0; }
  .abs { position: absolute; }

  /* front */
  .brand-front { left: 75px; top: 95px; display: flex; align-items: center; gap: 8px; }
  .brand-front .mark { width: 14px; height: 14px; background: var(--ink); }
  .brand-front .name { font-size: 15px; font-weight: 500; color: var(--ink); letter-spacing: .5px; }
  .headline { left: 16px; top: 305px; color: var(--paper); font-size: 22px; font-weight: 300; line-height: 26px; }
  .headline strong { color: var(--orange); font-weight: 700; display: block; }
  .headline .success { display: block; color: var(--orange); font-size: 34px; line-height: 38px; letter-spacing: 1px; }
  .headline-rule { left: 16px; top: 415px; width: 162px; height: 3px; background: var(--orange); }
  .front-copy { left: 16px; width: 330px; color: var(--paper); font-size: 11px; line-height: 15px; }
  .front-copy--a { top: 443px; }
  .front-copy--b { top: 500px; }
  .signup { left: 0; top: 552px; width: 473px; height: 118px; background: var(--paper); }
  .signup-frame { position: absolute; inset: 6px 5px 6px 5px; border: 1px dashed #555; }
  .signup-title { position: absolute; left: 0; right: 0; top: 14px; text-align: center; color: var(--orange-deep); font-size: 14px; font-weight: 500; }
  .signup-title span { border-bottom: 2px solid var(--ink); padding-bottom: 1px; }
  .field { position: absolute; left: 15px; width: 440px; height: 14px; display: flex; align-items: flex-end; gap: 8px; }
  .field label { color: var(--orange-deep); font-size: 10px; line-height: 12px; font-weight: 600; width: 98px; flex: none; white-space: nowrap; }
  .field .line { flex: 1; border-bottom: 1px solid #888; height: 1px; margin-bottom: 3px; }

  /* back */
  .brand-back { left: 22px; top: 302px; display: flex; align-items: center; gap: 8px; }
  .brand-back .mark { width: 20px; height: 20px; background: var(--orange); }
  .brand-back .name { font-size: 22px; line-height: 24px; font-weight: 400; color: var(--charcoal-dark); letter-spacing: .5px; }
  .intro { left: 22px; top: 342px; font-size: 14px; font-weight: 500; color: var(--charcoal-dark); }
  .pillar { width: 200px; }
  .pillar h3 { display: flex; align-items: center; gap: 8px; color: var(--orange-deep); font-size: 10px; font-weight: 600; margin-bottom: 8px; height: 20px; }
  .pillar h3 svg { width: 22px; height: 20px; }
  .pillar p { font-size: 8.2px; line-height: 11px; color: var(--ink); text-align: justify; }
  .footer { left: 0; top: 610px; width: 473px; height: 60px; background: var(--orange); }
  .social { position: absolute; top: 10px; left: 0; right: 0; display: flex; justify-content: center; gap: 11px; }
  .social span { width: 22px; height: 22px; border: 1.5px solid var(--paper); border-radius: 50%; }
  .url { position: absolute; top: 41px; left: 0; right: 0; text-align: center; color: var(--paper); font-size: 9px; }
</style>
</head>
<body>

<section class="sheet sheet--front" aria-label="Front side">
  <svg class="shapes" viewBox="0 0 473 670" width="473" height="670">
    <polygon points="0,0 340,0 0,330" fill="var(--orange-soft)"/>
    <polygon points="0,140 75,215 0,215" fill="var(--charcoal-dark)"/>
    <polygon points="0,215 120,215 0,300" fill="var(--orange-deep)"/>
    <polygon points="330,0 473,0 473,320 345,420 125,215" fill="#c9ccd0" role="img" aria-label="Photo of a presenter speaking to a seated audience in a bright office"/>
    <polygon points="125,215 330,0 340,0 133,215" fill="var(--orange)"/>
    <polyline points="125,215 345,420 473,320" fill="none" stroke="var(--paper)" stroke-width="3"/>
    <polygon points="355,430 473,338 473,360 366,444" fill="var(--orange)"/>
    <polygon points="380,460 473,390 473,540" fill="var(--charcoal-dark)"/>
  </svg>
  <div class="abs brand-front"><span class="mark"></span><span class="name">VERANTIS</span></div>
  <h1 class="abs headline">Learn simple<strong>Strategies</strong>to ensure your<span class="success">SUCCESS</span></h1>
  <div class="abs headline-rule"></div>
  <p class="abs front-copy front-copy--a">we host 6+ networking events in Denver throughout the year that are free to attend and are unlike any other networking event they've attended before</p>
  <p class="abs front-copy front-copy--b">we have in-person meetings 2x per month, virtual meeting options, networking events, and educational events</p>
  <div class="abs signup">
    <div class="signup-frame"></div>
    <p class="signup-title"><span>Join the Verantis Community Today!</span></p>
    <div class="field" style="top:40px"><label>Name :</label><span class="line"></span></div>
    <div class="field" style="top:55px"><label>Email Address :</label><span class="line"></span></div>
    <div class="field" style="top:70px"><label>Company Name :</label><span class="line"></span></div>
    <div class="field" style="top:85px"><label>Phone Number :</label><span class="line"></span></div>
  </div>
</section>

<section class="sheet sheet--back" aria-label="Back side">
  <svg class="shapes" viewBox="0 0 473 670" width="473" height="670">
    <polygon points="0,0 455,0 455,318 0,212" fill="#b9a48c" role="img" aria-label="Photo of hands reviewing business charts on a table"/>
    <polygon points="0,212 455,318 463,335 0,245" fill="var(--charcoal-dark)"/>
    <polygon points="0,245 463,335 465,345 0,270" fill="var(--orange)"/>
    <polygon points="0,270 160,300 0,290" fill="var(--charcoal)"/>
    <rect x="455" y="0" width="18" height="340" fill="var(--orange)"/>
    <line x1="237" y1="385" x2="237" y2="605" stroke="var(--orange)" stroke-width="1"/>
    <line x1="5" y1="492" x2="468" y2="492" stroke="var(--orange)" stroke-width="1"/>
  </svg>
  <div class="abs brand-back"><span class="mark"></span><span class="name">VERANTIS</span></div>
  <h2 class="abs intro">Verantis offers a four-pronged approach:</h2>

  <div class="abs pillar" style="left:22px;top:382px">
    <h3><svg viewBox="0 0 22 20"><circle cx="8" cy="6" r="4" fill="var(--orange-deep)"/><path d="M1 18c0-5 3-7 7-7s7 2 7 7z" fill="var(--orange-deep)"/><path d="M15 9l6 6M21 9l-6 6" stroke="var(--orange-deep)" stroke-width="2"/></svg>Collaboration</h3>
    <p>Work with like-minded, driven Verantis members to collaborate and overcome the objections, hurdles and challenges that all business professionals face, in either in person twice monthly meetings, or virtually, from the comfort of your home of office.</p>
  </div>
  <div class="abs pillar" style="left:255px;top:382px">
    <h3><svg viewBox="0 0 22 20"><path d="M1 4l2 2 3-4M1 10l2 2 3-4M1 16l2 2 3-4" stroke="var(--orange-deep)" stroke-width="1.5" fill="none"/><path d="M9 4h12M9 10h12M9 16h12" stroke="var(--orange-deep)" stroke-width="2"/></svg>Accountability</h3>
    <p>Stay on track, and complete the goals you have set for yourself! Weekly in person or virtual meetings afford all members the opportunity to review their plan twice a month with your fellow Verantis members and trained Verantis coaches, to make certain you success is continuous throughout the year.</p>
  </div>
  <div class="abs pillar" style="left:22px;top:506px">
    <h3><svg viewBox="0 0 22 20"><rect x="1" y="14" width="3" height="5" fill="var(--orange-deep)"/><rect x="6" y="10" width="3" height="9" fill="var(--orange-deep)"/><rect x="11" y="6" width="3" height="13" fill="var(--orange-deep)"/><rect x="16" y="1" width="3" height="18" fill="var(--orange-deep)"/></svg>Referrals</h3>
    <p>In the midst of crafting an executable, measurable and attainable plan let Verantis build your business through a steady stream of referral opportunities via twelve yearly networking events, specifically designed to ensure you walk away with new referral partners.</p>
  </div>
  <div class="abs pillar" style="left:255px;top:506px">
    <h3><svg viewBox="0 0 22 20"><polygon points="11,3 21,8 11,13 1,8" fill="var(--charcoal-dark)"/><path d="M5 10v5c2 2 10 2 12 0v-5l-6 3z" fill="var(--charcoal-dark)"/></svg>Strategy</h3>
    <p>Let Verantis assist you in crafting a strategy within our proven business planning template; realistic, understandable, measurable, beyond normal, attainable and time bound.</p>
  </div>

  <div class="abs footer">
    <div class="social" aria-label="Social links"><span></span><span></span><span></span><span></span></div>
    <p class="url">www.verantis-example.com</p>
  </div>
</section>

</body>
</html>
```